Product Label Design

We require 2 labels, with the same look and feel, designed for our range of trucking related products for the transport industry. Our logo has been provided.

In terms of the look and feel, we are after:
- a clean and elegant design to represent our premium range of products. By clean we mean not "too busy" or cluttered
- masculine as this relates to trucking,
- must convey that our products are cutting-edge and innovative (our competitors' labels are outdated and dull thus we want to stand-out in the world market)

We want you to create a standardised label template for us, which we can use for several products. We will simply change the product description and product code and reprint.

Each product label will have a:
• Product Description
• Product code
• An image or artwork of a truck as all our products are for the transport industry
• Display product Size in bottom right hand corner
Label 1: 20L (180 mm x 180 mm with 5 mm radius on corners )
Label 2: 750ml (A copy of the 750ml bottle die line has been unloaded as a PDF)

You may use text placeholders for the description.

Files Required:
We need the final design as a psd file, as our business uses Photoshop CS6.

REFERENCE:
Attached is an sample label with the features we want (ie product description, product size, and so on). Please DO NOT use or see this as a reference for your design or style we are after. We do not want your creativity to be restricted by this sample.

Target Market(s)

Products for the trucking industry

Industry/Entity Type

Industry

Colors

Designer to choose colors to be used in the design.

Requirements
Must have
• Logo
• • Image of a truck on the label (preferably the truck should be cutting edge and modern to align it with our product)
• • Some type of background
• • Product description
• • Product code
• • Product size on Bottom Right corner
Should not have
• Unnecessary graphics that will clutter the design

```html
<!DOCTYPE html>
<html lang="en">
<head>
<meta charset="utf-8">
<title>Product Label – 20L</title>
<link href="https://fonts.googleapis.com/css2?family=Montserrat:wght@400;500;700;800&display=swap" rel="stylesheet">
<style>
  :root {
    --sky: #22b6f7;
    --indigo: #6a52e6;
    --white: #ffffff;
    --sun-top: #ffe033;
    --sun-bottom: #ff8a52;
    --plum-a: #a23fb0;
    --plum-b: #c74a8a;
    --lime: #c9e34a;
    --teal: #38c2a6;
    --coral: #e8465c;
    --gold: #ffd21f;
    --amber: #ff9a2e;
    --photo-light: #eef1f6;
    --photo-mid: #b9c0cc;
  }
  * { margin: 0; padding: 0; box-sizing: border-box; }
  html, body { width: 1200px; height: 1200px; overflow: hidden; background: #ffffff; }
  .label {
    position: relative;
    width: 1200px;
    height: 1200px;
    overflow: hidden;
    border-radius: 34px;
    background: linear-gradient(180deg, var(--sky) 0%, #3c8ff2 40%, var(--indigo) 100%);
    font-family: "Montserrat", sans-serif;
    color: var(--white);
  }
  .decor { position: absolute; inset: 0; width: 1200px; height: 1200px; }
  .brand {
    position: absolute;
    left: 340px;
    top: 42px;
    width: 540px;
    display: flex;
    align-items: center;
    gap: 22px;
  }
  .brand-dot {
    width: 92px; height: 92px;
    border-radius: 50%;
    background: var(--white);
    flex: none;
  }
  .brand-name {
    font-weight: 800;
    font-size: 74px;
    line-height: 0.98;
    letter-spacing: 1px;
    text-transform: uppercase;
  }
  .product-title {
    position: absolute;
    left: 200px;
    top: 385px;
    width: 710px;
    text-align: center;
    font-weight: 700;
    font-size: 54px;
    letter-spacing: 9px;
    text-transform: uppercase;
  }
  .product-subtitle {
    position: absolute;
    left: 300px;
    top: 455px;
    width: 600px;
    text-align: center;
    font-weight: 500;
    font-size: 30px;
    letter-spacing: 3px;
  }
  .product-description {
    position: absolute;
    left: 132px;
    top: 562px;
    font-weight: 500;
    font-size: 29px;
    line-height: 36px;
    letter-spacing: 2.4px;
    white-space: pre;
  }
  .truck-photo {
    position: absolute;
    left: 355px;
    top: 752px;
    width: 820px;
    height: 448px;
    clip-path: polygon(30px 100px, 220px 85px, 453px 2px, 810px 20px, 800px 300px, 760px 432px, 40px 432px, 8px 350px, 12px 200px);
    background: linear-gradient(160deg, var(--photo-light) 0%, #dfe3ea 55%, var(--photo-mid) 100%);
  }
  .product-size {
    position: absolute;
    right: 14px;
    bottom: 14px;
    font-weight: 700;
    font-size: 34px;
    letter-spacing: 5px;
  }
</style>
</head>
<body>
  <main class="label">
    <svg class="decor" viewBox="0 0 1200 1200" aria-hidden="true">
      <defs>
        <linearGradient id="sun" x1="0" y1="0" x2="0" y2="1">
          <stop offset="0" stop-color="var(--sun-top)"/>
          <stop offset="1" stop-color="var(--sun-bottom)"/>
        </linearGradient>
        <linearGradient id="plum" x1="0" y1="0" x2="1" y2="1">
          <stop offset="0" stop-color="var(--plum-a)"/>
          <stop offset="1" stop-color="var(--plum-b)"/>
        </linearGradient>
        <linearGradient id="meadow" x1="0" y1="0" x2="0" y2="1">
          <stop offset="0" stop-color="var(--teal)"/>
          <stop offset="1" stop-color="var(--lime)"/>
        </linearGradient>
        <linearGradient id="flare" x1="0" y1="0" x2="0" y2="1">
          <stop offset="0" stop-color="var(--gold)"/>
          <stop offset="1" stop-color="var(--amber)"/>
        </linearGradient>
      </defs>
      <circle class="sun-disc" cx="227" cy="452" r="157" fill="url(#sun)"/>
      <rect class="plum-pill" x="960" y="540" width="300" height="620" rx="150"
            transform="rotate(18 1110 850)" fill="url(#plum)"/>
      <polygon class="meadow-wedge" points="0,960 240,862 240,1200 0,1200" fill="url(#meadow)"/>
      <path class="coral-wave" d="M760 1200 L790 1080 Q900 1030 1100 1060 L1110 1200 Z" fill="var(--coral)"/>
      <polygon class="gold-corner" points="1100,1010 1200,1000 1200,1200 1055,1200" fill="url(#flare)"/>
      <polygon class="accent-slash" points="925,356 950,362 912,500 888,494" fill="url(#sun)"/>
      <g class="bracket" fill="none" stroke="var(--white)" stroke-width="7">
        <line x1="933" y1="47" x2="933" y2="234"/>
        <polyline points="933,145 1043,145 1043,422 938,422"/>
      </g>
    </svg>

    <div class="brand">
      <span class="brand-dot"></span>
      <span class="brand-name">Tarven<br>Freight</span>
    </div>

    <h1 class="product-title">Label Text Here</h1>
    <p class="product-subtitle">Short Description Here</p>

    <p class="product-description">Lorem ipsum dolor sit amet, consectetur
adipiscing elit, sed do eiusmod tempor
incididunt ut labore et dolore magna
aliqua. Ut enim ad minim veniam, quis
nostrud exercitation ullamco laboris
nisi ut aliquip exea
commodo
consequat.</p>

    <div class="truck-photo" role="img" aria-label="Photo of a modern white semi-trailer truck"></div>

    <p class="product-size">20L</p>
  </main>
</body>
</html>
```